Vesk Architecture

We are a architectural design and build company working between scales 1/1000 to 1/1 we want people to understand our difference from our design experience and quality.we build hotels restourants and office spaces.Our company name is Vesk architecture to mind sustainability.

We want to write our adress phone and work spesifications on the card and we want our logo as backround.

Ps:you could find the logo adress and phone box numbers from the web:www.veskmimarlik-ornek.com

Target Market(s)

Who looks for experts.

Industry/Entity Type

Architecture

Requirements
Must have
• Design is over everything.
Should not have
• we don want it to be colorfull

```html
<!DOCTYPE html>
<html lang="tr">
<head>
<meta charset="utf-8">
<title>Vesk Mimarlık – Kartvizit</title>
<link href="https://fonts.googleapis.com/css2?family=Barlow:wght@300;400;500&display=swap" rel="stylesheet">
<style>
  :root {
    --paper: #ffffff;
    --frame: #c9c9c9;
    --card-edge: #b8b8b8;
    --plum: #5a4649;
    --plum-glow: #8a7a7c;
    --ink: #6b5a5c;
    --accent: #8c4a44;
    --muted: #a49497;
    --white: #ffffff;
  }
  * { margin: 0; padding: 0; box-sizing: border-box; }
  html, body {
    width: 1200px; height: 901px; overflow: hidden;
    background: var(--paper);
    font-family: "Barlow", Arial, sans-serif;
  }
  .sheet {
    position: relative; width: 1200px; height: 901px;
    border: 2px solid var(--frame);
  }
  .card {
    position: absolute; left: 256px; width: 680px;
    border: 1px solid var(--card-edge);
    overflow: hidden;
  }
  .card--front {
    top: 28px; height: 389px;
    background: radial-gradient(circle at 50% 48%, var(--plum-glow) 0%, var(--plum) 38%, var(--plum) 100%);
    display: flex; align-items: center; justify-content: center;
  }
  .front-name {
    color: var(--white); font-weight: 300; font-size: 96px;
    letter-spacing: 4px; line-height: 1;
  }
  .card--back { top: 490px; height: 392px; background: var(--paper); }
  .back-band {
    position: absolute; left: 0; top: 0; width: 100%; height: 196px;
    background: var(--plum);
    box-shadow: 0 6px 10px rgba(0,0,0,0.18);
  }
  .wordmark {
    position: absolute; left: 48px; top: 42px; color: var(--white); font-weight: 300;
  }
  .wordmark__name { display: block; font-size: 84px; line-height: 1; letter-spacing: 2px; }
  .wordmark__sub { display: block; font-size: 16px; letter-spacing: 3px; margin-top: 14px; }
  .holder {
    position: absolute; left: 45px; top: 251px;
    font-size: 17px; font-weight: 500; color: var(--ink);
  }
  .holder__role { color: var(--accent); }
  .contact {
    position: absolute; left: 338px; top: 246px;
    font-size: 15px; font-weight: 500; color: var(--ink); line-height: 24px;
  }
  .contact__address { margin-bottom: 8px; }
  .contact__label { color: var(--muted); display: inline-block; width: 18px; }
</style>
</head>
<body>
  <main class="sheet">
    <section class="card card--front">
      <span class="front-name">vesk</span>
    </section>

    <section class="card card--back">
      <div class="back-band">
        <div class="wordmark">
          <span class="wordmark__name">vesk</span>
          <span class="wordmark__sub">MİMARLIK</span>
        </div>
      </div>
      <p class="holder">Deniz Arman YILMAZ - <span class="holder__role">Mimar</span></p>
      <div class="contact">
        <p class="contact__address">Kestane Mah. Liman Cad. Gül Sok.<br>No : 7 Kadıköy / İSTANBUL</p>
        <p><span class="contact__label">t.</span> 0216 555 01 23</p>
        <p><span class="contact__label">f.</span> 0216 555 01 24</p>
        <p><span class="contact__label">e.</span>veskmimarlik@ornek-posta.com</p>
      </div>
    </section>
  </main>
</body>
</html>
```